8" x 11" One Page Flyer for Fence Installation Company

We are looking to promote our business with a new flyer that would be handed out in person to people or put at their mailbox/door at their homes. The flyer needs to be creative and attention-grabbing. I have attached some of our previous flyers and our website information. Do not call or email regarding the flyer. We want the flyer to look professional but also friendly. One page, NOT folded. You can use images from our website at www.MyBraxtonYard.com or our Facebook page at www.Facebook.com/HollowbrookRailsBKT. We are flexible with what photos you can use but there must be photos of OUR fences on the flyer. More photos specifically can also be provided. Colors need to be suitable for a flyer printed on canary yellow in color paper OR white paper.

Target Market(s)

Homeowners that need a new fence

Industry/Entity Type

Construction

Font styles to use
Sans Serif
Other font styles liked:
• HD Colton

Colors
0054AA
0677BA
7BADD7
CADEEF
E8F1F8
0094D4
00A9DD
6FCCEA
C7EBF8
E9F6FB

Requirements
Must have
• Our fence photos - mostly wood fence photos (different designs), SIZE SHOULD BE LETTER SIZE 8" x 11"
Nice to have
• A nice bible verse featured at the bottom of the flyer.
Should not have
• DO NOT COPY THE WEBSITE FORMAT, I WANT SOMETHING UNIQUE. Other people's fence photos, they must all come from our website or facebook page

```html
<!DOCTYPE html>
<html lang="en">
<head>
<meta charset="utf-8">
<title>Hollowbrook Rails – Fence Flyer</title>
<link href="https://fonts.googleapis.com/css2?family=Russo+One&family=PT+Sans:wght@400;700&display=swap" rel="stylesheet">
<style>
:root{
  --orange:#e88f2e;
  --orange-deep:#d97d1c;
  --blue:#3a7cc4;
  --ink:#2b2b2b;
  --paper:#ffffff;
  --stage:#ececec;
  --wood:#c79a5e;
  --leaf:#4f7a3a;
}
*{box-sizing:border-box;margin:0;padding:0}
html,body{width:1200px;height:2378px;overflow:hidden;background:var(--stage)}
.flyer{
  position:absolute;left:50px;top:475px;width:734px;height:952px;
  transform:scale(1.4986);transform-origin:0 0;
  background:var(--paper);overflow:hidden;
  font-family:"PT Sans",Arial,sans-serif;color:var(--ink);
}
.hero-panel{
  position:absolute;left:0;top:0;width:431px;height:368px;
  border-bottom-right-radius:42px;
  background:linear-gradient(135deg,#e99a3e 0%,#e48a28 55%,#d97d1c 100%);
}
.headline{
  position:absolute;left:60px;top:102px;
  font-family:"Russo One",Arial,sans-serif;color:#fff;
  font-size:58px;line-height:55px;letter-spacing:-1px;
}
.tagline{
  position:absolute;left:63px;top:245px;color:#fff;
  font-weight:700;font-size:20px;line-height:23px;
}
.hero-photo{
  position:absolute;left:431px;top:-20px;width:330px;height:490px;
  background:var(--paper);border-radius:120px 0 0 0;
}
.hero-photo .fill{
  position:absolute;left:16px;top:20px;right:0;bottom:20px;
  border-radius:110px 0 0 0;
  background:linear-gradient(180deg,#3f6b33 0%,#5d8a45 40%,#b99258 75%,#a58a6a 100%);
}
.side-accent{
  position:absolute;left:656px;top:463px;width:78px;height:240px;
  background:var(--orange);border-bottom-left-radius:78px 120px;
}
.why{position:absolute;left:78px;top:420px;width:250px}
.why h2{color:var(--blue);font-size:21px;font-weight:700}
.why .lead{color:var(--orange);font-size:16px;line-height:20px;margin-top:6px}
.benefits{list-style:none;margin-top:13px}
.benefits li{font-size:12.5px;height:22.6px;display:flex;align-items:center;gap:5px}
.benefits svg{width:9px;height:9px;flex:none}
.location{position:absolute;left:340px;top:398px;width:130px}
.address{
  margin:0 auto;width:100px;background:var(--blue);color:#fff;
  font-size:8.5px;line-height:9px;text-align:center;padding:3px 0;
  clip-path:polygon(6% 0,94% 0,100% 100%,0 100%);
}
.map{
  margin-top:2px;height:98px;border-radius:8px;
  background:linear-gradient(160deg,#eef0f1,#dfe3e5 60%,#e8eaeb);
  box-shadow:0 2px 6px rgba(0,0,0,.18);position:relative;
}
.map .pin{position:absolute;left:57px;top:40px}
.pointer{width:0;height:0;margin:4px auto 0;border-left:6px solid transparent;border-right:6px solid transparent;border-top:9px solid #e3e3e3}
.showroom{position:absolute;left:312px;top:570px;width:320px}
.showroom p{color:var(--orange);font-size:15.5px;line-height:20px}
.hours{margin-top:11px;font-size:12px;line-height:21px;padding-left:2px}
.gallery{position:absolute;left:78px;top:700px;display:flex;gap:6px}
.gallery div{width:111px;height:116px;border-radius:22px 4px 22px 4px}
.g1{background:linear-gradient(180deg,#4f7a3a,#a98a62)}
.g2{background:linear-gradient(180deg,#5a8046,#8a6a48)}
.g3{background:linear-gradient(180deg,#3f6b33,#c79a5e)}
.g4{background:linear-gradient(180deg,#c89f66,#b48650)}
.g5{background:linear-gradient(180deg,#dcd8d0,#c9a26a)}
.brand{position:absolute;left:78px;top:832px;display:flex;align-items:flex-start;gap:10px}
.brand-dot{width:14px;height:14px;border-radius:50%;background:var(--orange);margin-top:8px}
.brand-name{font-size:22px;font-weight:700;color:var(--blue);line-height:24px}
.brand-phone{font-size:20px;font-weight:700;line-height:22px}
.brand-motto{font-size:7px;font-weight:700;margin-top:3px}
.contact{position:absolute;left:365px;font-size:9.5px;line-height:12px}
.contact .label{color:var(--blue);font-weight:700;display:flex;align-items:center;gap:5px}
.contact .value{padding-left:17px}
.email{top:853px}
.call{top:890px}
.web{position:absolute;left:513px;top:902px;font-size:9.5px;display:flex;align-items:center;gap:4px}
.footer-band{position:absolute;left:0;top:925px;width:734px;height:27px}
</style>
</head>
<body>
<main class="flyer">
  <section class="hero-panel" role="img" aria-label="Orange-toned photo of a split rail fence post">
    <h1 class="headline">WE BUILD<br>FENCES....</h1>
    <p class="tagline">And we would love to build<br>your fence too!</p>
  </section>

  <div class="hero-photo"><div class="fill" role="img" aria-label="Photo of an arched wooden garden gate on a split rail fence"></div></div>
  <div class="side-accent"></div>

  <section class="why">
    <h2>Why Choose Us?</h2>
    <p class="lead">Beautiful, professionally installed fencesat affordable prices!</p>
    <ul class="benefits">
      <li><svg viewBox="0 0 10 10"><circle cx="5" cy="5" r="4.2" fill="none" stroke="#e88f2e" stroke-width="1.1"/><path d="M3 5.2l1.5 1.4L7.2 3.6" fill="none" stroke="#e88f2e" stroke-width="1.2"/></svg>Free Estimates</li>
      <li><svg viewBox="0 0 10 10"><circle cx="5" cy="5" r="4.2" fill="none" stroke="#e88f2e" stroke-width="1.1"/><path d="M3 5.2l1.5 1.4L7.2 3.6" fill="none" stroke="#e88f2e" stroke-width="1.2"/></svg>Professional Installation</li>
      <li><svg viewBox="0 0 10 10"><circle cx="5" cy="5" r="4.2" fill="none" stroke="#e88f2e" stroke-width="1.1"/><path d="M3 5.2l1.5 1.4L7.2 3.6" fill="none" stroke="#e88f2e" stroke-width="1.2"/></svg>Concrete in EVERY Post</li>
      <li><svg viewBox="0 0 10 10"><circle cx="5" cy="5" r="4.2" fill="none" stroke="#e88f2e" stroke-width="1.1"/><path d="M3 5.2l1.5 1.4L7.2 3.6" fill="none" stroke="#e88f2e" stroke-width="1.2"/></svg>HOA Submission Assistance</li>
      <li><svg viewBox="0 0 10 10"><circle cx="5" cy="5" r="4.2" fill="none" stroke="#e88f2e" stroke-width="1.1"/><path d="M3 5.2l1.5 1.4L7.2 3.6" fill="none" stroke="#e88f2e" stroke-width="1.2"/></svg>Lifetime Workmanship Warranty</li>
      <li><svg viewBox="0 0 10 10"><circle cx="5" cy="5" r="4.2" fill="none" stroke="#e88f2e" stroke-width="1.1"/><path d="M3 5.2l1.5 1.4L7.2 3.6" fill="none" stroke="#e88f2e" stroke-width="1.2"/></svg>Experienced Installation Teams</li>
      <li><svg viewBox="0 0 10 10"><circle cx="5" cy="5" r="4.2" fill="none" stroke="#e88f2e" stroke-width="1.1"/><path d="M3 5.2l1.5 1.4L7.2 3.6" fill="none" stroke="#e88f2e" stroke-width="1.2"/></svg>Quality Workmanship &amp; Materials</li>
      <li><svg viewBox="0 0 10 10"><circle cx="5" cy="5" r="4.2" fill="none" stroke="#e88f2e" stroke-width="1.1"/><path d="M3 5.2l1.5 1.4L7.2 3.6" fill="none" stroke="#e88f2e" stroke-width="1.2"/></svg>FREE Gate Adjustments for LIFE</li>
    </ul>
  </section>

  <section class="location">
    <div class="address">418 Crestline Ave<br>Braxton, NC 28204</div>
    <div class="map" role="img" aria-label="Street map showing the showroom location">
      <svg class="pin" width="12" height="16" viewBox="0 0 12 16"><path d="M6 0a6 6 0 0 1 6 6c0 4-6 10-6 10S0 10 0 6a6 6 0 0 1 6-6z" fill="#e03a2f"/><circle cx="6" cy="6" r="2.2" fill="#a3221a"/></svg>
    </div>
    <div class="pointer"></div>
  </section>

  <section class="showroom">
    <p>Visit our indoor &amp; outdoor&nbsp; showroom! Our outdoor showroom is open 24/7, while our indoor showroom and office is open</p>
    <div class="hours">Monday -Thurs 9AM - 3PM,<br>Friday 9AM - 1PM</div>
  </section>

  <section class="gallery">
    <div class="g1" role="img" aria-label="Photo of a three-rail wooden fence with wire mesh"></div>
    <div class="g2" role="img" aria-label="Photo of a tall privacy fence along a garden bed"></div>
    <div class="g3" role="img" aria-label="Photo of a split rail fence with a company sign"></div>
    <div class="g4" role="img" aria-label="Photo of a wooden privacy gate"></div>
    <div class="g5" role="img" aria-label="Photo of a wooden picket fence beside a house"></div>
  </section>

  <section class="brand">
    <span class="brand-dot"></span>
    <div>
      <div class="brand-name">Hollowbrook Rails</div>
      <div class="brand-phone">555-014-2268</div>
      <div class="brand-motto">"Because Good Fences Make Good Neighbors"</div>
    </div>
  </section>

  <div class="contact email">
    <div class="label"><svg width="11" height="8" viewBox="0 0 11 8"><rect x="0.5" y="0.5" width="10" height="7" fill="none" stroke="#3a7cc4"/><path d="M.5.5l5 4 5-4" fill="none" stroke="#3a7cc4"/></svg>Email Address:</div>
    <div class="value">office@mybraxtonyard.com</div>
  </div>
  <div class="contact call">
    <div class="label"><svg width="11" height="11" viewBox="0 0 11 11"><path d="M2.2 1l2 2-1.1 1.4a6 6 0 0 0 3.5 3.5L8 6.8l2 2-1.3 1.6C4.6 10 1 6.4.6 2.3z" fill="#3a7cc4"/></svg>Call Us:</div>
    <div class="value">555-014-2268</div>
  </div>
  <div class="web">
    <svg width="11" height="11" viewBox="0 0 11 11"><circle cx="5.5" cy="5.5" r="4.8" fill="none" stroke="#3a7cc4"/><ellipse cx="5.5" cy="5.5" rx="2" ry="4.8" fill="none" stroke="#3a7cc4"/><path d="M.7 5.5h9.6" stroke="#3a7cc4"/></svg>
    www.MyBraxtonYard.com
  </div>

  <svg class="footer-band" viewBox="0 0 734 27" preserveAspectRatio="none">
    <rect x="0" y="15" width="734" height="12" fill="#3a7cc4"/>
    <polygon points="0,0 252,0 270,27 0,27" fill="#3a7cc4"/>
  </svg>
</main>
</body>
</html>
```